Letterhead Design Project

Consulting Company , we want a letterhead incorporating both the picture provided and the logo provided. The font name is monotype corsiva.
Target Market(s)
Dentist
Industry/Entity Type
Consulting
Font styles to use
Other font styles liked:
- monotype corsiva

Colors
0455a3
Requirements
Must have
- the logo, the picture (see attached), the website name, the email. and the phone numbers.
- Website: www.trquillarisadvisory.solutions
- Email: will be provided to the winner, please use placeholder
- Phone numbers:
- Petra Hallum 5829017763
- Owen Vrastik 6148250397

Nice to have
- a swoop or wave across the bottom. a line up the side. I don't know guys. design something unique and professional.

Should not have
- arrows pointing off the logo or anywhere. no arrows. our logo altered in anyway. no broken circles. no variences in blue. we like our logo the way it is. the font is monotype corsiva

```html
<!DOCTYPE html>
<html lang="en">
<head>
<meta charset="utf-8">
<title>Trquillaris Advisory Letterhead</title>
<link rel="stylesheet" href="https://fonts.googleapis.com/css2?family=Cormorant+Garamond:ital,wght@1,500&family=Tinos&family=Montserrat:wght@500&display=swap">
<style>
  :root {
    --brand-blue: #0455a3;
    --brand-blue-soft: #dce8f4;
    --ink: #3a3a3a;
    --ink-soft: #666666;
    --rule-dark: #2f3437;
    --paper: #ffffff;
    --backdrop: #e6e6e6;
  }
  * { margin: 0; padding: 0; box-sizing: border-box; }
  html, body { width: 1200px; height: 831px; overflow: hidden; }
  body { background: var(--backdrop); position: relative; font-family: "Tinos", "Times New Roman", serif; color: var(--ink); }

  .letterhead {
    position: absolute; left: 320px; top: 20px; width: 560px; height: 792px;
    background: var(--paper); box-shadow: 0 2px 10px rgba(0,0,0,0.12);
  }

  .brand { position: absolute; left: 40px; top: 38px; display: flex; align-items: center; gap: 10px; }
  .brand__mark { width: 44px; height: 44px; border: 2px solid var(--brand-blue); border-radius: 50%; flex: none; }
  .brand__name {
    font-family: "Cormorant Garamond", "Times New Roman", serif; font-style: italic; font-weight: 500;
    font-size: 19px; color: var(--brand-blue); white-space: nowrap;
  }

  .client-picture {
    position: absolute; right: 40px; top: 30px; width: 130px; height: 60px;
    background: linear-gradient(135deg, var(--brand-blue-soft), #b9cfe6);
  }

  .recipient { position: absolute; left: 56px; top: 140px; font-family: "Cormorant Garamond", serif; font-style: italic; font-weight: 500; }
  .recipient__name { font-size: 18px; color: var(--ink); }
  .recipient__line { font-size: 10.5px; color: var(--ink-soft); letter-spacing: 0.4px; line-height: 1.25; }

  .body-copy { position: absolute; left: 56px; top: 205px; width: 450px; font-size: 7.6px; line-height: 1.45; color: var(--ink-soft); }
  .body-copy p { margin-bottom: 9px; text-align: justify; }

  .signature { position: absolute; right: 56px; top: 415px; text-align: center; }
  .signature__name { font-family: "Cormorant Garamond", serif; font-style: italic; font-weight: 500; font-size: 18px; color: var(--ink); }
  .signature__role { font-family: "Montserrat", sans-serif; font-weight: 500; font-size: 7px; letter-spacing: 1.6px; color: var(--ink-soft); }

  .contact-row {
    position: absolute; left: 30px; right: 30px; top: 668px;
    display: flex; justify-content: space-between; align-items: flex-start;
  }
  .contact-item { width: 125px; text-align: center; font-size: 7.4px; line-height: 1.35; color: var(--ink); }
  .contact-item svg { display: block; margin: 0 auto 7px; height: 24px; width: 24px; }

  .footer-rule--blue { position: absolute; left: 30px; right: 30px; top: 738px; height: 3px; background: var(--brand-blue); }
  .footer-rule--dark { position: absolute; left: 30px; right: 30px; top: 745px; height: 2px; background: var(--rule-dark); }
</style>
</head>
<body>
  <main class="letterhead">
    <header class="brand">
      <span class="brand__mark" aria-hidden="true"></span>
      <span class="brand__name">Trquillaris Advisory, LLC</span>
    </header>
    <div class="client-picture" role="img" aria-label="Client-supplied picture for the letterhead"></div>

    <section class="recipient">
      <div class="recipient__name">Miles Arden</div>
      <div class="recipient__line">CEO, ARDEN STUDIO</div>
      <div class="recipient__line">M: +1 555 014 2290</div>
    </section>

    <section class="body-copy">
      <p>Thank you for the opportunity to support your dental practice. Our advisors review operations, staffing, billing and patient flow, then prepare a clear plan with practical steps, agreed timelines and measurable goals that your team can follow with confidence each month.</p>
      <p>During the first review we meet with owners and staff, study current systems, and note where time or revenue is lost. Every finding is shared openly, ranked by impact, and paired with a simple action you can start right away.</p>
      <p>Compliance remains central to our work. We check records, consent forms, infection control routines and privacy practices against current rules, and we train your staff so that good habits stay in place long after our visit ends.</p>
      <p>Please contact us with any questions about this proposal. We look forward to working with you and your team.</p>
    </section>

    <section class="signature">
      <div class="signature__name">Your Name</div>
      <div class="signature__role">DIRECTOR</div>
    </section>

    <footer>
      <div class="contact-row">
        <div class="contact-item">
          <svg viewBox="0 0 24 24" aria-hidden="true"><path d="M12 2a7 7 0 0 0-7 7c0 5 7 13 7 13s7-8 7-13a7 7 0 0 0-7-7z" fill="var(--brand-blue)"/><circle cx="12" cy="9" r="2.6" fill="#fff"/></svg>
          418 Alder Lane Bowling Green,<br>Kentucky 42101
        </div>
        <div class="contact-item">
          <svg viewBox="0 0 24 24" aria-hidden="true"><path d="M6.6 3.5l3 .4 1.2 4-2 1.6a11 11 0 0 0 5.7 5.7l1.6-2 4 1.2.4 3c0 1.2-1 2.1-2.2 2A17 17 0 0 1 4.6 5.7c-.1-1.2.8-2.2 2-2.2z" fill="var(--brand-blue)"/></svg>
          Petra Hallum 5829017763<br>Owen Vrastik 6148250397
        </div>
        <div class="contact-item">
          <svg viewBox="0 0 24 24" aria-hidden="true"><rect x="2" y="5" width="20" height="14" rx="1.5" fill="var(--brand-blue)"/><path d="M3 6l9 7 9-7" fill="none" stroke="#fff" stroke-width="1.6"/></svg>
          info@trquillarisadvisory.solutions
        </div>
        <div class="contact-item">
          <svg viewBox="0 0 24 24" aria-hidden="true"><circle cx="12" cy="12" r="10" fill="var(--brand-blue)"/><ellipse cx="12" cy="12" rx="4" ry="9" fill="none" stroke="#fff" stroke-width="1.3"/><path d="M3 12h18M5 7.5h14M5 16.5h14" stroke="#fff" stroke-width="1.2"/></svg>
          www.trquillarisadvisory.solutions
        </div>
      </div>
      <div class="footer-rule--blue"></div>
      <div class="footer-rule--dark"></div>
    </footer>
  </main>
</body>
</html>
```